Urgent seeking Cover Design for event

An Outdoor Movie Event company in singapore is seeking for a Cover Design to be placed on Lumoket for an outdoor movie event at a location called Marrowgate Plaza.
Cover design size is 920px by 450px
We have provided images in this project for your side to come out with something suitable but not too complicated.
We urgently need the design which can be in PDF format for easy editing on our ends. We also need all readable and editable working files.

Target Market(s)

movie goers

Colors

Designer to choose colors to be used in the design.

Requirements
Must have
• Simple design to incorporate images provided if able to.
Nice to have
• Cover size to be 920px by 450px
Should not have
• Not be too messy

```html
<!DOCTYPE html>
<html lang="en">
<head>
<meta charset="utf-8">
<title>Outdoor Movie Event Cover</title>
<link href="https://fonts.googleapis.com/css2?family=Cinzel:wght@400;500&family=Montserrat:wght@600&family=Questrial&display=swap" rel="stylesheet">
<style>
  :root {
    --maroon: #5e0c14;
    --white: #ffffff;
    --sky-top: #3f6fb4;
    --sky-mid: #9fb7d6;
    --park-dark: #1f3a1c;
    --lawn: #3d7a2c;
    --plaza-top: #7fb4d8;
    --plaza-mid: #2d6f9a;
    --fountain: #2ec4cf;
  }
  * { margin: 0; padding: 0; box-sizing: border-box; }
  html, body { width: 1200px; height: 587px; overflow: hidden; background: var(--white); }
  .cover { position: relative; width: 1200px; height: 587px; overflow: hidden; font-family: 'Questrial', sans-serif; color: var(--white); }
  .park-photo {
    position: absolute; inset: 0;
    background: linear-gradient(180deg, var(--sky-top) 0%, var(--sky-mid) 28%, var(--park-dark) 48%, #2c4f25 62%, var(--lawn) 80%, #2f6524 100%);
  }
  .bands { position: absolute; inset: 0; }
  .brand-box {
    position: absolute; left: 74px; top: 55px; width: 408px; height: 95px;
    background: var(--maroon); text-align: center; padding-top: 11px;
  }
  .brand-name { font-family: 'Cinzel', serif; font-weight: 400; font-size: 50px; line-height: 1; letter-spacing: 1px; }
  .brand-sub { font-family: 'Cinzel', serif; font-weight: 500; font-size: 12px; letter-spacing: 1.6px; margin-top: 6px; }
  .headline {
    position: absolute; left: 74px; top: 188px;
    font-family: 'Montserrat', sans-serif; font-weight: 600; font-size: 47px; line-height: 1;
    letter-spacing: -0.5px;
  }
  .venue-photo {
    position: absolute; left: 759px; top: 13px; width: 430px; height: 430px; border-radius: 50%;
    border: 9px solid var(--white);
    background: linear-gradient(180deg, var(--plaza-top) 0%, #cfe3ef 30%, var(--plaza-mid) 55%, #c9a64a 68%, var(--fountain) 80%, #0f4f6b 100%);
  }
  .social { position: absolute; left: 39px; top: 520px; display: flex; gap: 11px; }
  .social-dot { width: 44px; height: 44px; border-radius: 50%; background: var(--white); }
  .tagline { position: absolute; left: 223px; top: 519px; font-size: 17.2px; line-height: 22px; width: 520px; }
  .details {
    position: absolute; left: 782px; top: 459px; width: 372px;
    font-size: 18px; line-height: 21.8px; text-align: justify; text-align-last: justify;
  }
</style>
</head>
<body>
<div class="cover">
  <div class="park-photo" role="img" aria-label="Evening outdoor movie screening on a park lawn, people on picnic mats facing an inflatable screen under a cloudy blue sky"></div>

  <svg class="bands" width="1200" height="587" viewBox="0 0 1200 587" aria-hidden="true">
    <path d="M0 412 C120 470 230 500 320 497 C470 492 640 420 805 375 C930 345 1060 340 1200 330 L1200 587 L0 587 Z" fill="var(--maroon)"/>
    <path d="M0 412 C120 470 230 500 320 497 C470 492 640 420 805 375 C930 345 1060 340 1200 330" fill="none" stroke="var(--white)" stroke-width="6"/>
  </svg>

  <div class="brand-box">
    <div class="brand-name">SOLVANE</div>
    <div class="brand-sub">SOLVANE EVENTS PTE LTD</div>
  </div>

  <h1 class="headline">LOREM IPSUM DOLOR SITE</h1>

  <div class="venue-photo" role="img" aria-label="Marrowgate Plaza at dusk, glass canopy above a lit shopfront with turquoise floor fountains"></div>

  <div class="social" aria-label="Social media">
    <span class="social-dot"></span>
    <span class="social-dot"></span>
    <span class="social-dot"></span>
  </div>

  <p class="tagline">Lorem ipsum dolor sit amet, consectetuer adipiscing elit, sed diam nonummy nibh euismod tincidunt ut laoreet dolore lore</p>

  <p class="details">Lorem ipsum dolor sit amet, consectetuer adipiscing elit, sed diam nonummy nibh euismod tincidunt ut laoreet dolore magna aliquam erat volutpat. Ut wisi enim ad minim veniam, quis nostrud</p>
</div>
</body>
</html>
```